Editorial Website Design for High-End Custom Millwork Firm

Design (no development) for a 5-7 page website for a high-end custom architectural millwork firm. Editorial, magazine-quality aesthetic — think Dwelling Quarterly and top-tier millwork studios (Owen Tallard, Vorko). Full brief, reference sites, and project photography attached. We have uploaded a sample of our photography to use in your design. PLEASE READ PDF DOCUMENT BRIEF!!!

```html
<!DOCTYPE html>
<html lang="en">
<head>
<meta charset="utf-8">
<title>Oakline Millwork — Home</title>
<link href="https://fonts.googleapis.com/css2?family=Cormorant+Garamond:wght@400;500&family=Inter:wght@400;500;600&display=swap" rel="stylesheet">
<style>
:root{
  --backdrop:#000;
  --paper:#f6f5f1;
  --paper-2:#f1f0ec;
  --white:#ffffff;
  --ink:#2a2825;
  --muted:#7b776f;
  --rule:#d9d6cf;
  --dark:#222120;
  --dark-rule:#3b3936;
  --light-text:#eeebe4;
}
*{margin:0;padding:0;box-sizing:border-box}
html,body{width:1200px;height:1200px;overflow:hidden;background:var(--backdrop)}
.stage{position:absolute;left:0;top:0;width:1932px;height:1932px;transform:scale(.621118);transform-origin:0 0}
.page{position:absolute;left:786px;top:0;width:359px;height:1932px;background:var(--paper);overflow:hidden;font-family:'Inter',sans-serif;color:var(--ink)}
.abs{position:absolute}
.serif{font-family:'Cormorant Garamond',serif;font-weight:400}
.caps{text-transform:uppercase;letter-spacing:.14em}
.photo{position:absolute}
.tag{position:absolute;background:#fff;font-size:3.2px;letter-spacing:.12em;padding:1.5px 3px;text-transform:uppercase;color:var(--ink)}

/* hero */
.hero{position:absolute;left:0;top:0;width:359px;height:212px;background:linear-gradient(160deg,#4a4a3c 0%,#5b5244 35%,#7b7263 60%,#3e3a33 100%)}
.hero-shade{position:absolute;inset:0;background:linear-gradient(90deg,rgba(20,18,15,.55),rgba(20,18,15,.1))}
.logo{left:16px;top:6px;font-size:10px;color:#fff;letter-spacing:.04em}
.nav{right:14px;top:9px;display:flex;gap:9px;font-size:5px;color:#fff;letter-spacing:.04em}
.hero-eyebrow{left:20px;top:63px;font-size:4.2px;color:#e9e5dc}
.hero-title{left:20px;top:74px;font-size:26px;line-height:24px;color:#fff;width:190px}
.hero-inset{left:204px;top:90px;width:140px;height:138px;background:linear-gradient(180deg,#ece8df 0%,#d9c6a2 45%,#b99667 100%)}
.hero-dots{left:210px;top:215px;display:flex;gap:4px}
.hero-dots span{width:4px;height:4px;border-radius:50%;border:.6px solid #fff}
.hero-dots span:first-child{background:#fff}
.hero-next{left:327px;top:210px;width:17px;height:18px;background:#3b3835}

/* intro */
.intro-rule{left:20px;top:240px;width:20px;height:.6px;background:var(--rule)}
.intro-label{left:20px;top:251px;font-size:3.6px;color:var(--muted)}
.intro-head{left:130px;top:240px;width:205px;font-size:14px;line-height:19px;color:var(--ink)}
.intro-body{left:130px;top:330px;width:142px;font-size:5px;line-height:9px;color:var(--muted)}
.link{font-size:3.8px;font-weight:600;letter-spacing:.12em;text-transform:uppercase;color:var(--ink)}

/* category */
.cat-rule{left:4px;top:433px;width:22px;height:.7px;background:var(--ink)}
.cat-title{left:34px;top:427px;font-size:9.5px;letter-spacing:.04em}
.cat-list{left:34px;top:448px;list-style:none;font-size:4.3px;letter-spacing:.14em;text-transform:uppercase;color:var(--muted)}
.cat-list li{height:18px}
.cat-photo{left:135px;top:415px;width:206px;height:186px;background:linear-gradient(180deg,#f1eee8 0%,#dcc7a3 45%,#a9b8ac 70%,#b47d4f 100%)}

/* works */
.section-title{font-size:13px}
.work-title{font-size:8px}
.work-meta{font-size:4.2px;letter-spacing:.14em;text-transform:uppercase;color:var(--muted)}

/* capabilities */
.caps-band{position:absolute;left:0;top:1316px;width:359px;height:244px;background:var(--dark)}
.cap-list{left:195px;top:1400px;width:144px;list-style:none}
.cap-list li{height:20.5px;border-top:.6px solid var(--dark-rule);font-size:3.8px;letter-spacing:.12em;text-transform:uppercase;color:var(--light-text);padding-top:8px}
.cap-list li:last-child{border-bottom:.6px solid var(--dark-rule)}
.badge{position:absolute;border:1.2px solid #d8d4cc;border-radius:50%}

/* social */
.social-band{position:absolute;left:0;top:1560px;width:359px;height:237px;background:var(--white)}
.tile{position:absolute;top:1639px;width:76px;height:134px}
.tile .plus{position:absolute;right:5px;top:5px;width:7px;height:7px;border-radius:50%;background:#fff}
.tile .handle{position:absolute;left:5px;bottom:8px;font-size:3.6px;color:#fff;font-weight:600;line-height:5px}
.tile .handle small{display:block;font-weight:400;opacity:.8}

/* footer */
.footer{position:absolute;left:0;top:1797px;width:359px;height:135px;background:var(--paper-2)}
.foot-links{left:187px;top:1827px;list-style:none;font-size:4.6px;font-weight:500;letter-spacing:.06em}
.foot-links li{height:12.5px}
.foot-contact{left:271px;top:1827px;font-size:4px;line-height:5.6px;color:var(--muted)}
.foot-rule{left:20px;top:1902px;width:319px;height:.6px;background:var(--rule)}
.legal{font-size:3.4px;letter-spacing:.12em;text-transform:uppercase;color:var(--muted)}
</style>
</head>
<body>
<div class="stage">
<main class="page">

  <!-- hero -->
  <section class="hero" role="img" aria-label="Craftsman assembling a timber frame in a workshop"><div class="hero-shade"></div></section>
  <div class="abs serif logo">OLM</div>
  <nav class="abs nav"><span>Projects</span><span>Capabilities</span><span>About</span><span>Blog</span><span>Contact</span></nav>
  <p class="abs caps hero-eyebrow">Est. 2008 — Durham, North Carolina</p>
  <h1 class="abs serif hero-title">Award-quality custom architectural millwork.</h1>
  <div class="photo hero-inset" role="img" aria-label="Light oak kitchen with pendant lights and view to a garden"></div>
  <div class="abs hero-dots"><span></span><span></span><span></span><span></span></div>
  <div class="abs hero-next"></div>

  <!-- intro -->
  <div class="abs intro-rule"></div>
  <p class="abs caps intro-label">AMG Premium Grade</p>
  <h2 class="abs serif intro-head">We produce high-end commercial interiors and residential built-ins for architects, interior designers, and discerning homeowners.</h2>
  <p class="abs intro-body">Operating at the intersection of traditional craftsmanship and modern fabrication, Oakline Millwork delivers uncompromising precision for the most demanding spaces.</p>
  <span class="abs link" style="left:284px;top:330px">Read our story →</span>

  <!-- categories -->
  <div class="abs cat-rule"></div>
  <h3 class="abs serif cat-title">DINING</h3>
  <ul class="abs cat-list">
    <li>Boardroom</li><li>Conference</li><li>Desks</li><li>Credenzas and Lecterns</li>
    <li>Moot Courts</li><li>Benches and Banquettes</li><li>Collaborative</li><li>Product Lines</li>
  </ul>
  <div class="photo cat-photo" role="img" aria-label="Oak kitchen island with sage upholstered stools"></div>
  <span class="tag" style="left:197px;top:421px">Commercial</span>
  <span class="abs link" style="left:254px;top:635px">Browse custom furniture &nbsp;→</span>

  <!-- selected works -->
  <h2 class="abs serif section-title" style="left:20px;top:667px">Selected Works</h2>

  <div class="photo" style="left:20px;top:703px;width:150px;height:187px;background:linear-gradient(180deg,#3d3a36 0%,#8a6a4a 40%,#c7b59a 65%,#2b2a28 100%)" role="img" aria-label="Hotel retail boutique with arched wood shelving"></div>
  <span class="tag" style="left:26px;top:709px">Commercial</span>
  <h3 class="abs serif work-title" style="left:20px;top:898px">The Linden Hotel &amp; Spa</h3>
  <p class="abs work-meta" style="left:20px;top:912px">Cary, NC — Lobby &amp; Corridors</p>

  <div class="photo" style="left:190px;top:733px;width:149px;height:149px;background:linear-gradient(160deg,#6e5038 0%,#a79478 40%,#e3e0da 70%,#7a86a8 100%)" role="img" aria-label="Arched built-in china cabinet with blue and white dishes"></div>
  <span class="tag" style="left:196px;top:739px">Residential</span>
  <h3 class="abs serif work-title" style="left:190px;top:891px">Foxglove Residence</h3>
  <p class="abs work-meta" style="left:190px;top:907px">Chapel Hill, NC — Built-ins &amp; Library</p>

  <div class="photo" style="left:20px;top:932px;width:319px;height:119px;background:linear-gradient(90deg,#8a6a38 0%,#b9955a 25%,#5e4630 50%,#6f6a63 75%,#4e4740 100%)" role="img" aria-label="Hotel reception desk and lounge with wood paneling"></div>
  <div class="photo" style="left:20px;top:1000px;width:319px;height:51px;background:linear-gradient(180deg,rgba(0,0,0,0),rgba(0,0,0,.45))"></div>
  <h3 class="abs serif" style="left:35px;top:1012px;font-size:12px;color:#f3efe6">The Ashgrove Hotel</h3>
  <p class="abs work-meta" style="left:35px;top:1030px;color:#d8d2c6">Commercial · Hospitality · Durham, NC</p>

  <div class="photo" style="left:20px;top:1071px;width:150px;height:153px;background:linear-gradient(160deg,#5f7488 0%,#8ea0b0 45%,#c9b48a 75%,#d9d3c8 100%)" role="img" aria-label="Blue painted pantry cabinetry with glazed door"></div>
  <span class="tag" style="left:26px;top:1077px">Residential</span>
  <h3 class="abs serif work-title" style="left:20px;top:1233px">The Kestrel</h3>
  <p class="abs work-meta" style="left:20px;top:1247px">Cary, NC — Lobby &amp; Corridors</p>

  <div class="photo" style="left:190px;top:1085px;width:149px;height:173px;background:linear-gradient(180deg,#e8e2d6 0%,#ddd3c2 45%,#c7ad8a 75%,#a98a66 100%)" role="img" aria-label="Cream kitchen with oak island and brass pendants"></div>
  <span class="tag" style="left:196px;top:1091px">Residential</span>
  <h3 class="abs serif work-title" style="left:190px;top:1267px">Foxglove Residence</h3>
  <p class="abs work-meta" style="left:190px;top:1282px">Chapel Hill, NC — Built-ins &amp; Library</p>

  <span class="abs link" style="left:20px;top:1283px">View portfolio →</span>

  <!-- capabilities -->
  <section class="caps-band"></section>
  <div class="photo" style="left:20px;top:1333px;width:145px;height:151px;background:linear-gradient(150deg,#cfd2d6 0%,#4f6e8f 40%,#8a6d52 75%,#c98b4a 100%)" role="img" aria-label="Craftsman in welding mask grinding a panel"></div>
  <div class="photo" style="left:92px;top:1428px;width:88px;height:108px;background:linear-gradient(180deg,#efece6 0%,#c9a77c 50%,#a98358 100%)" role="img" aria-label="Curved oak vanity cabinet"></div>
  <h2 class="abs serif section-title" style="left:195px;top:1332px;color:var(--light-text)">Capabilities</h2>
  <p class="abs" style="left:195px;top:1359px;width:140px;font-size:4.8px;line-height:9px;color:#b8b3aa">We manage complex architectural millwork scopes from engineering through installation, maintaining premium quality at every step.</p>
  <ul class="abs cap-list">
    <li>Veneer matching &amp; panel systems</li>
    <li>Custom cabinetry &amp; casework</li>
    <li>Moulding &amp; trim</li>
    <li>Finishing &amp; professional installation</li>
  </ul>
  <div class="badge" style="left:195px;top:1495px;width:39px;height:39px"></div>
  <div class="abs" style="left:240px;top:1497px;width:58px;height:36px;border:1.2px solid #d8d4cc"></div>
  <div class="badge" style="left:304px;top:1495px;width:40px;height:40px"></div>

  <!-- social -->
  <section class="social-band"></section>
  <p class="abs caps" style="left:0;width:359px;text-align:center;top:1601px;font-size:3.6px;color:var(--muted)">As seen on Clipstream</p>
  <h2 class="abs serif section-title" style="left:0;width:359px;text-align:center;top:1610px">Custom Architectural Millwork</h2>
  <div class="tile" style="left:23px;background:linear-gradient(160deg,#e6e4e0,#9a8a74 60%,#3d3a36)" role="img" aria-label="Craftsman sanding a chair frame"><span class="plus"></span><p class="handle">@oakline_mill<small>12.4K likes</small></p></div>
  <div class="tile" style="left:103px;background:linear-gradient(160deg,#7f96a0,#c9cdd0 50%,#5e5a55)" role="img" aria-label="Grey bathroom vanity"><span class="plus"></span><p class="handle">@bench_notes<small>8.1K likes</small></p></div>
  <div class="tile" style="left:183px;background:linear-gradient(160deg,#e7a35a,#c06a2b 50%,#8a4a22)" role="img" aria-label="Wood library shelving in warm light"><span class="plus"></span><p class="handle">@grain_room<small>5.6K likes</small></p></div>
  <div class="tile" style="left:263px;background:linear-gradient(160deg,#8a5a34,#c78a4a 40%,#3f3f6a 80%)" role="img" aria-label="Lounge with wood screen and blue sofa"><span class="plus"></span><p class="handle">@oak_and_line<small>9.3K likes</small></p></div>

  <!-- footer -->
  <footer class="footer"></footer>
  <h2 class="abs serif" style="left:20px;top:1826px;font-size:8.5px">Oakline Millwork</h2>
  <p class="abs" style="left:20px;top:1845px;width:105px;font-size:3.8px;line-height:6.5px;color:var(--muted)">Award-quality custom architectural millwork and cabinetry based in Durham, North Carolina. AMG Premium Grade.</p>
  <ul class="abs foot-links"><li>Projects</li><li>Capabilities</li><li>About</li><li>Blog</li></ul>
  <p class="abs foot-contact">48 Foundry Lane<br>Durham, NC 27705<br><br>info@oaklinemillwork.com<br><br>919.555.0142</p>
  <div class="abs foot-rule"></div>
  <p class="abs legal" style="left:20px;top:1912px">© 2025 Oakline Millwork. All rights reserved.</p>
  <p class="abs legal" style="left:287px;top:1912px">Privacy Policy &nbsp;&nbsp;&nbsp; Terms</p>

</main>
</div>
</body>
</html>
```